Larkspur Realty

Business cards for 4 people

They need to say for all
57 Danner Quay, Boston MA 02117

Each person will have their own personal information
We would like gold embossing for the name of the company
Mabel is the blonde sitting in the chair smiling her information should be on the back of the card with her name and information
Should say for slogan classic pattern, elevated experience
mabel@larkspurhomesnet.com
(413) 555-0182

Odessa is the brunette with wavy hair in the tan suit odessa@larkspurhomesnet.com
(617) 555-0147

june@larkspurhomesnet.com
(413) 555-0169
standing next to the chair

ruth@larkspurhomesnet.com
(413) 555-0193
close up headshot

```html
<!DOCTYPE html>
<html lang="en">
<head>
<meta charset="utf-8">
<title>Larkspur Realty – Business Cards</title>
<link rel="stylesheet" href="https://fonts.googleapis.com/css2?family=Cinzel:wght@400;500&family=Cormorant+Garamond:wght@400;500&family=Great+Vibes&display=swap">
<style>
  :root {
    --backdrop: #111b33;
    --card: #233352;
    --gold: #e8b356;
    --gold-light: #f6d58e;
    --gold-deep: #c48a2e;
    --shadow: rgba(0, 0, 0, 0.45);
  }
  html, body {
    margin: 0;
    padding: 0;
    width: 848px;
    height: 1200px;
    overflow: hidden;
    background: var(--backdrop);
  }
  .sheet {
    position: relative;
    width: 848px;
    height: 1200px;
    background: var(--backdrop);
    font-family: "Cinzel", serif;
    color: var(--gold);
  }

  /* Brand panel */
  .brand-panel {
    position: absolute;
    left: 298px;
    top: 28px;
    width: 267px;
    height: 153px;
    background: var(--card);
    text-align: center;
  }
  .brand-panel .brand-ring {
    position: absolute;
    left: 50%;
    top: 12px;
    width: 78px;
    height: 78px;
    margin-left: -41px;
    border: 2px solid var(--gold);
    border-radius: 50%;
  }
  .brand-panel .brand-name {
    position: absolute;
    left: 0;
    right: 0;
    top: 104px;
    margin: 0;
    font-size: 21px;
    font-weight: 400;
    letter-spacing: 0.5px;
    color: var(--gold);
    white-space: nowrap;
  }

  /* Cards */
  .card {
    position: absolute;
    width: 333px;
    height: 204px;
    background: var(--card);
    box-shadow: 0 3px 6px var(--shadow);
    overflow: hidden;
  }
  .card.front { left: 68px; }
  .card.back  { left: 460px; }
  .row-1 { top: 217px; }
  .row-2 { top: 446px; }
  .row-3 { top: 675px; }
  .row-4 { top: 903px; }

  /* Front */
  .portrait {
    position: absolute;
    left: 10px;
    top: 54px;
    width: 106px;
    height: 106px;
    border-radius: 50%;
    padding: 2px;
    background: linear-gradient(135deg, var(--gold-light), var(--gold-deep) 50%, var(--gold-light));
  }
  .portrait .photo {
    width: 100%;
    height: 100%;
    border-radius: 50%;
  }
  .photo.blonde   { background: radial-gradient(circle at 50% 35%, #efe9e2 0%, #d9cbb5 45%, #2a2624 100%); }
  .photo.brunette { background: radial-gradient(circle at 50% 40%, #d8b8a6 0%, #8c6a58 45%, #2b211e 100%); }
  .photo.tan-suit { background: radial-gradient(circle at 50% 35%, #f4efe9 0%, #c79a74 50%, #8a5d3c 100%); }
  .photo.standing { background: radial-gradient(circle at 50% 35%, #f3f1ee 0%, #b49c87 50%, #3a2c24 100%); }

  .front .brand-block {
    position: absolute;
    left: 138px;
    width: 184px;
    top: 52px;
    text-align: center;
  }
  .front .brand-ring {
    display: block;
    width: 42px;
    height: 42px;
    margin: 0 auto;
    border: 1.5px solid var(--gold);
    border-radius: 50%;
  }
  .front .brand-name {
    margin: 8px 0 0;
    font-size: 14px;
    font-weight: 400;
    letter-spacing: 0.3px;
    white-space: nowrap;
    color: var(--gold);
  }
  .front .address {
    margin: 7px 0 0;
    font-family: "Cormorant Garamond", serif;
    font-variant: small-caps;
    font-size: 9.5px;
    font-weight: 500;
    letter-spacing: 0.4px;
    white-space: nowrap;
    color: var(--gold);
  }

  /* Back */
  .back .details {
    position: absolute;
    left: 0;
    right: 0;
    top: 68px;
    text-align: center;
  }
  .back .slogan {
    margin: 0;
    font-family: "Great Vibes", cursive;
    font-size: 24px;
    font-weight: 400;
    line-height: 1;
    color: var(--gold);
  }
  .back .email {
    margin: 7px 0 0;
    font-family: "Cinzel", serif;
    font-size: 8.5px;
    letter-spacing: 0.3px;
    line-height: 1.2;
    text-transform: uppercase;
  }
  .back .phone {
    margin: 2px 0 0;
    font-family: "Cormorant Garamond", serif;
    font-size: 10.5px;
    line-height: 1.2;
  }
  .back .mini-brand {
    position: absolute;
    left: 0;
    right: 0;
    top: 170px;
    text-align: center;
  }
  .back .mini-brand .brand-ring {
    display: block;
    width: 11px;
    height: 11px;
    margin: 0 auto;
    border: 1px solid var(--gold);
    border-radius: 50%;
  }
  .back .mini-brand .brand-name {
    margin: 2px 0 0;
    font-size: 4.5px;
    letter-spacing: 0.2px;
    white-space: nowrap;
  }
</style>
</head>
<body>
<main class="sheet">

  <section class="brand-panel">
    <span class="brand-ring"></span>
    <h1 class="brand-name">LARKSPUR REALTY</h1>
  </section>

  <!-- Mabel -->
  <article class="card front row-1">
    <div class="portrait"><div class="photo blonde" role="img" aria-label="Portrait of Mabel, blonde, smiling, seated in a chair"></div></div>
    <div class="brand-block">
      <span class="brand-ring"></span>
      <h2 class="brand-name">LARKSPUR REALTY</h2>
      <p class="address">57 Danner Quay, Boston MA 02117</p>
    </div>
  </article>
  <article class="card back row-1">
    <div class="details">
      <p class="slogan">Elevated Experience</p>
      <p class="email">mabel@larkspurhomesnet.com</p>
      <p class="phone">(413) 555-0182</p>
    </div>
    <div class="mini-brand"><span class="brand-ring"></span><p class="brand-name">LARKSPUR REALTY</p></div>
  </article>

  <!-- Ruth -->
  <article class="card front row-2">
    <div class="portrait"><div class="photo brunette" role="img" aria-label="Close-up headshot of Ruth"></div></div>
    <div class="brand-block">
      <span class="brand-ring"></span>
      <h2 class="brand-name">LARKSPUR REALTY</h2>
      <p class="address">57 Danner Quay, Boston MA 02117</p>
    </div>
  </article>
  <article class="card back row-2">
    <div class="details">
      <p class="slogan">Elevated Experience</p>
      <p class="email">ruth@larkspurhomesnet.com</p>
      <p class="phone">(413) 555-0193</p>
    </div>
    <div class="mini-brand"><span class="brand-ring"></span><p class="brand-name">LARKSPUR REALTY</p></div>
  </article>

  <!-- Odessa -->
  <article class="card front row-3">
    <div class="portrait"><div class="photo tan-suit" role="img" aria-label="Portrait of Odessa, brunette with wavy hair in a tan suit"></div></div>
    <div class="brand-block">
      <span class="brand-ring"></span>
      <h2 class="brand-name">LARKSPUR REALTY</h2>
      <p class="address">57 Danner Quay, Boston MA 02117</p>
    </div>
  </article>
  <article class="card back row-3">
    <div class="details">
      <p class="slogan">Elevated Experience</p>
      <p class="email">odessa@larkspurhomesnet.com</p>
      <p class="phone">(617) 555-0147</p>
    </div>
    <div class="mini-brand"><span class="brand-ring"></span><p class="brand-name">LARKSPUR REALTY</p></div>
  </article>

  <!-- June -->
  <article class="card front row-4">
    <div class="portrait"><div class="photo standing" role="img" aria-label="Portrait of June standing next to a chair"></div></div>
    <div class="brand-block">
      <span class="brand-ring"></span>
      <h2 class="brand-name">LARKSPUR REALTY</h2>
      <p class="address">57 Danner Quay, Boston MA 02117</p>
    </div>
  </article>
  <article class="card back row-4">
    <div class="details">
      <p class="slogan">Elevated Experience</p>
      <p class="email">june@larkspurhomesnet.com</p>
      <p class="phone">(413) 555-0169</p>
    </div>
    <div class="mini-brand"><span class="brand-ring"></span><p class="brand-name">LARKSPUR REALTY</p></div>
  </article>

</main>
</body>
</html>
```